Need a simple blog where questions can be posted and answered by the community. I already have something started in WordPress. www.brimfernalerts.com. I cannot figure out how to make the blog functionality work the way I want. It is IMPORTANT the designer code it in the existing wordpress account.

```html
<!DOCTYPE html>
<html lang="en">
<head>
<meta charset="utf-8">
<title>Brimfern COVID-19 Partner &amp; Industry Forum</title>
<link href="https://fonts.googleapis.com/css2?family=Lato:wght@300;400;700;900&display=swap" rel="stylesheet">
<style>
:root{
  --navy:#2d2a5e;
  --blue:#3a66a8;
  --sky:#1f9be0;
  --orange:#e98a2c;
  --red:#d9302c;
  --ink:#2b2b2b;
  --muted:#777;
  --line:#d6d6d6;
  --page:#efefef;
  --chip:#eceef3;
  --footer:#3a3562;
}
*{box-sizing:border-box;margin:0;padding:0}
html,body{width:964px;height:1200px;overflow:hidden}
body{font-family:'Lato',sans-serif;background:var(--page);color:var(--ink);position:relative}
.site-header{position:absolute;left:0;top:0;width:964px;height:91px;background:#fff}
.brand{position:absolute;left:140px;top:20px;display:flex;align-items:center;gap:10px}
.brand-mark{width:42px;height:42px;background:var(--navy)}
.brand-name{font-weight:900;font-size:14.5px;line-height:16px;color:var(--navy)}
.brand-name span{display:block;color:var(--blue);font-weight:700}
.nav{position:absolute;left:481px;top:28px;display:flex;align-items:center;height:35px}
.nav a{font-size:12px;color:#555;text-decoration:none;margin-right:31px;position:relative}
.nav a.active{color:var(--blue)}
.nav a.active::after{content:"";position:absolute;left:0;right:0;top:44px;height:3px;background:var(--blue);opacity:.6}
.nav a.cta{background:var(--blue);color:#fff;width:115px;height:35px;display:flex;align-items:center;justify-content:center;margin:0 0 0 -10px}
.hero{position:absolute;left:0;top:91px;width:964px;height:264px;color:#fff;text-align:center}
.hero-bg{position:absolute;inset:0;background:radial-gradient(circle at 20% 30%,#3a66a8 0,transparent 40%),radial-gradient(circle at 80% 60%,#3a66a8 0,transparent 35%),linear-gradient(#2a4f8e,#1f3f7a)}
.hero h1{position:relative;font-size:20.5px;font-weight:700;line-height:32px;padding-top:42px;width:700px;margin:0 auto}
.hero p{position:relative;font-size:16px;font-weight:700;line-height:22px;width:640px;margin:22px auto 0}
.hero .follow{position:relative;display:inline-flex;align-items:center;gap:6px;margin-top:16px;border:1px solid #fff;height:29px;padding:0 6px;font-size:10px}
.follow .sq{width:14px;height:14px;background:#fff}
.section-title{display:flex;align-items:center;font-size:15px;font-weight:700;color:var(--navy)}
.section-title::after{content:"";flex:1;height:1px;background:#9bb3d3;margin-left:11px}
.categories{position:absolute;left:140px;top:398px;width:450px}
.cat-grid{display:flex;justify-content:space-between;margin-top:22px}
.cat{width:106px;height:56px;background:#fff;border:1px solid var(--line);display:flex;align-items:center;justify-content:center;font-weight:700;font-size:13px}
.all-q{position:absolute;left:140px;top:520px;width:453px}
.filter{display:flex;gap:7px;font-size:8px;color:var(--muted);margin-left:10px}
.filter b{color:var(--ink)}
.filter .on{border-bottom:2px solid var(--red);color:var(--ink)}
.search{margin-top:14px;height:26px;background:#fff;border:1px solid var(--line);display:flex;align-items:center;justify-content:space-between;padding:0 7px;font-size:9.5px;font-weight:300;color:#999}
.q-list{margin-top:13px;background:#fff;border:1px solid var(--line)}
.q-item{height:91px;border-bottom:1px solid var(--line);position:relative}
.q-icon{position:absolute;left:20px;top:17px;width:32px;height:32px;border-radius:50%;border:1.5px solid var(--sky);display:flex;align-items:center;justify-content:center}
.q-icon.open{border-color:var(--orange);color:var(--orange);font-weight:900;font-size:14px}
.q-text{position:absolute;left:63px;top:17px;width:228px;font-size:8.6px;line-height:11px}
.q-meta{position:absolute;left:62px;top:63px;font-size:7.5px;color:#555;display:flex;align-items:center;gap:4px}
.q-meta i{width:12px;height:12px;border-radius:50%;border:1px solid #bbb}
.q-meta em{font-style:normal;color:var(--red)}
.stats{position:absolute;left:329px;top:17px;display:flex;gap:5px}
.stat{width:32px;text-align:center;font-size:7.5px;color:var(--muted)}
.stat b{display:flex;width:31px;height:31px;border-radius:50%;background:var(--chip);align-items:center;justify-content:center;color:var(--blue);font-size:9px;margin-bottom:7px}
.pager{height:30px;background:#e6e6e6;display:flex;align-items:center;justify-content:center;gap:12px;font-size:10px}
.pager .on{border-bottom:2px solid var(--red)}
.pager .arr{color:var(--red);font-size:14px}
.sidebar{position:absolute;left:614px;top:390px;width:208px;height:688px;background:#fff;border:1px solid var(--line);padding:15px 13px}
.ask{height:35px;background:var(--blue);color:#fff;font-weight:700;font-size:11.5px;display:flex;align-items:center;justify-content:center}
.send{text-align:center;font-size:8.8px;line-height:11.5px;margin-top:11px}
.side-title{display:flex;align-items:center;font-size:10.5px;font-weight:700;color:var(--navy);margin-top:15px;padding-left:3px}
.side-title::after{content:"";flex:1;height:1px;background:#9bb3d3;margin-left:9px}
.news{list-style:none;margin-top:10px;padding-left:4px;width:174px}
.news li{font-size:9.8px;line-height:12px;padding:6px 0;border-bottom:1px solid #e4e4e4}
.news li span{display:block;width:168px}
.news li:last-child{border:0}
.cat-list{list-style:none;margin-top:16px}
.cat-list li{display:flex;align-items:center;justify-content:space-between;font-size:10px;font-weight:700;height:24.5px;padding-left:4px}
.cat-list li span::before{content:"";display:inline-block;width:3px;height:3px;background:var(--red);margin-right:8px;vertical-align:middle}
.cat-list li b{width:17px;height:17px;border-radius:50%;background:var(--chip);color:var(--blue);font-size:7px;display:flex;align-items:center;justify-content:center}
.site-footer{position:absolute;left:0;top:1122px;width:964px;height:78px;background:var(--footer);color:#fff;font-size:11.5px;display:flex;align-items:center;justify-content:center}
</style>
</head>
<body>
<header class="site-header">
  <div class="brand"><div class="brand-mark"></div><div class="brand-name">BRIMFERN COVID-19<span>PARTNER &amp; INDUSTRY FORUM</span></div></div>
  <nav class="nav"><a class="active">HOME</a><a>ABOUT</a><a>QUESTIONS</a><a class="cta">ASK A QUESTION</a></nav>
</header>

<section class="hero">
  <div class="hero-bg" role="img" aria-label="Blue background of magnified virus particles"></div>
  <h1>This site is designed for our valued partners and industry associates to connect and share COVID-19 information.</h1>
  <p>Be sure to check out our Netlink page! There is more information from many more contributors</p>
  <span class="follow"><span class="sq"></span>Follow on Netlink</span>
</section>

<section class="categories">
  <h2 class="section-title">QUESTION CATEGORIES</h2>
  <div class="cat-grid"><div class="cat">PPE</div><div class="cat">PROTOCOLS</div><div class="cat">DATA</div><div class="cat">INSPIRATION</div></div>
</section>

<section class="all-q">
  <div style="display:flex;align-items:center;width:450px"><h2 class="section-title" style="flex:1">ALL QUESTIONS</h2>
    <div class="filter"><b>Filter:</b><span class="on">All</span><span>Open</span><span>Closed</span><span>Unanswered</span></div></div>
  <div class="search">What do you want to know?
    <svg width="14" height="14" viewBox="0 0 14 14"><circle cx="8" cy="6" r="4.5" fill="none" stroke="#333" stroke-width="1.2"/><path d="M4.8 9.2 1 13" stroke="#333" stroke-width="1.2"/></svg></div>
  <div class="q-list">
    <div class="q-item"><div class="q-icon"><svg width="14" height="12" viewBox="0 0 14 12"><path d="M6 1 1 5l5 4V6.5c3 0 5 1 6.5 4C12 6 10 3.8 6 3.5z" fill="#1f9be0"/></svg></div>
      <p class="q-text">What measures are you taking when forced by a state to take back a resident sent to the hospital and subsequently diagnosed with COVID19?</p>
      <div class="q-meta"><i></i>by <em>admin</em> asked 2 dayes ago &nbsp;|&nbsp; Inspiration</div>
      <div class="stats"><div class="stat"><b>20</b>Views</div><div class="stat"><b>3</b>Answers</div><div class="stat"><b>10</b>Votes</div></div></div>
    <div class="q-item"><div class="q-icon open">?</div>
      <p class="q-text">How do we protect against a potential land grab by unions leveraging this time as an opportunity to grab members?</p>
      <div class="q-meta"><i></i>by <em>admin</em> asked 3 dayes ago &nbsp;|&nbsp; Data</div>
      <div class="stats"><div class="stat"><b>11</b>Views</div><div class="stat"><b>1</b>Answers</div><div class="stat"><b>0</b>Votes</div></div></div>
    <div class="q-item"><div class="q-icon"><svg width="14" height="12" viewBox="0 0 14 12"><path d="M6 1 1 5l5 4V6.5c3 0 5 1 6.5 4C12 6 10 3.8 6 3.5z" fill="#1f9be0"/></svg></div>
      <p class="q-text">What measures are you taking when forced by a state to take back a resident sent to the hospital and subsequently diagnosed with COVID19?</p>
      <div class="q-meta"><i></i>by <em>admin</em> asked 5 dayes ago &nbsp;|&nbsp; PPE</div>
      <div class="stats"><div class="stat"><b>8</b>Views</div><div class="stat"><b>3</b>Answers</div><div class="stat"><b>2</b>Votes</div></div></div>
    <div class="q-item"><div class="q-icon open">?</div>
      <p class="q-text">How do we protect against a potential land grab by unions leveraging this time as an opportunity to grab members?</p>
      <div class="q-meta"><i></i>by <em>admin</em> asked 2 dayes ago &nbsp;|&nbsp; Protocols</div>
      <div class="stats"><div class="stat"><b>11</b>Views</div><div class="stat"><b>1</b>Answers</div><div class="stat"><b>0</b>Votes</div></div></div>
    <div class="q-item"><div class="q-icon"><svg width="14" height="12" viewBox="0 0 14 12"><path d="M6 1 1 5l5 4V6.5c3 0 5 1 6.5 4C12 6 10 3.8 6 3.5z" fill="#1f9be0"/></svg></div>
      <p class="q-text">What measures are you taking when forced by a state to take back a resident sent to the hospital and subsequently diagnosed with COVID19?</p>
      <div class="q-meta"><i></i>by <em>admin</em> asked 2 dayes ago &nbsp;|&nbsp; Data</div>
      <div class="stats"><div class="stat"><b>8</b>Views</div><div class="stat"><b>3</b>Answers</div><div class="stat"><b>2</b>Votes</div></div></div>
    <div class="pager"><span class="arr">&#8249;</span><span>1</span><span class="on">2</span><span>3</span><span>4</span><span class="arr">&#8250;</span></div>
  </div>
</section>

<aside class="sidebar">
  <div class="ask">+&nbsp; ASK YOUR QUESTION</div>
  <p class="send">Or send your questions to dana.reyes@brimfern.com and we will be sure to post them.</p>
  <h3 class="side-title">Latest News</h3>
  <ul class="news">
    <li><span>Coronavirus (COVID-19) current situation and case numbers</span></li>
    <li><span>Coronavirus (COVID-19) health alert</span></li>
    <li><span>COVID-19 Information for workplaces</span></li>
    <li><span>COVID-19 (Coronavirus) statistics</span></li>
    <li><span>Information sharing on COVID-19 Halvorn Health Bureau</span></li>
    <li><span>Coronavirus (COVID-19) events as they happen</span></li>
    <li><span>COVID-19 (Coronavirus) statistics</span></li>
    <li><span>COVID-19 Information for workplaces</span></li>
    <li><span>Coronavirus (COVID-19) current situation and case numbers</span></li>
  </ul>
  <h3 class="side-title" style="margin-top:28px">Categories</h3>
  <ul class="cat-list">
    <li><span>PPE</span><b>6</b></li>
    <li><span>Protocols</span><b>3</b></li>
    <li><span>Data</span><b>12</b></li>
    <li><span>Inspiration</span><b>13</b></li>
  </ul>
</aside>

<footer class="site-footer">© Copyright 2020 BRIMFERN COVID-19 PARTNER &amp; INDUSTRY FORUM. All Rights Reserved</footer>
</body>
</html>
```